Industrial Project Sign

We need an eye catching (but professional) industrial project sign that will be very large (roughly 12' high x 18' wide). This sign will be highly visible from the adjacent high speed highway.

* The following needs to be at the bottom of the signage: Logo (uploaded), Name (Pillar Ventures Group, Inc.) (uploaded) and phone number (555)613-8874

*Name of Project - "Brambleford Industrial Center"

* Text items
Land for Sale
Build to Suit
Zoning: Industrial (G I & L I)

* Interesting background that is eye catching
Updates

Good morning all,

We are considering all designers options as we go and are waiting for the final designs to come in by the 4th so that we can give each one a good look.   If you have any new designs, questions, further design options or any tweeks you want to do to current designs, please do so at this time.

Thanks to all of you for your submissions.

Industry/Entity Type

Industrial

```html
<!DOCTYPE html>
<html lang="en">
<head>
<meta charset="utf-8">
<title>Brambleford Industrial Center – Land for Sale</title>
<link href="https://fonts.googleapis.com/css2?family=Open+Sans:wght@400;600;700;800&display=swap" rel="stylesheet">
<style>
  :root {
    --maroon: #6b1014;
    --white: #ffffff;
    --ink: #141414;
    --grey-text: #3a3a3a;
    --bg-light: #e6e6e6;
    --bg-mid: #a9a9a9;
    --bg-dark: #6f6f6f;
    --panel-light: #e9e9eb;
  }
  html, body {
    margin: 0;
    padding: 0;
    width: 1200px;
    height: 800px;
    overflow: hidden;
    background: #ffffff;
  }
  .sign {
    position: relative;
    width: 1200px;
    height: 800px;
    overflow: hidden;
    font-family: "Open Sans", Arial, sans-serif;
    background: radial-gradient(ellipse 700px 650px at 110px 400px, #fbfbfb 0%, var(--bg-light) 30%, var(--bg-mid) 75%, #8f8f8f 100%);
  }
  .shapes {
    position: absolute;
    inset: 0;
  }
  .project-title {
    position: absolute;
    top: 30px;
    left: 0;
    width: 1200px;
    margin: 0;
    text-align: center;
    color: var(--white);
    font-weight: 800;
    font-size: 55px;
    letter-spacing: 1px;
    line-height: 1;
    text-shadow: 0 2px 3px rgba(0,0,0,.35);
  }
  .site-photo {
    position: absolute;
    left: 515px;
    top: 128px;
  }
  .headline {
    position: absolute;
    left: 600px;
    width: 600px;
    margin: 0;
    text-align: center;
    font-weight: 800;
    line-height: 1;
  }
  .headline--maroon {
    color: var(--maroon);
    font-size: 50px;
    text-shadow: 0 1px 1px rgba(255,255,255,.25);
  }
  .land-for-sale { top: 258px; }
  .build-to-suit { top: 496px; }
  .zoning {
    top: 350px;
    color: var(--white);
    font-weight: 700;
    font-size: 46px;
    line-height: 1.1;
    text-shadow: 0 2px 3px rgba(0,0,0,.35);
  }
  .zoning .code { color: var(--maroon); text-shadow: none; }
  .inquiry {
    position: absolute;
    left: 560px;
    width: 640px;
    text-align: center;
  }
  .inquiry-label {
    top: 575px;
    color: var(--grey-text);
    font-size: 40px;
    font-weight: 400;
    line-height: 1;
  }
  .inquiry-phone {
    top: 625px;
    color: var(--maroon);
    font-size: 78px;
    font-weight: 700;
    line-height: 1;
    letter-spacing: 1px;
  }
  .brand-mark {
    position: absolute;
    left: 80px;
    top: 270px;
    width: 440px;
    display: flex;
    align-items: center;
    gap: 22px;
  }
  .brand-square {
    width: 90px;
    height: 90px;
    background: var(--maroon);
    flex: none;
  }
  .brand-name {
    color: var(--maroon);
    font-weight: 800;
    font-size: 44px;
    line-height: 1.08;
  }
  .company-name {
    position: absolute;
    left: 22px;
    top: 620px;
    margin: 0;
    color: var(--ink);
    font-weight: 600;
    font-size: 24px;
  }
  .website {
    position: absolute;
    top: 740px;
    left: 0;
    width: 1200px;
    text-align: center;
    font-weight: 800;
    font-size: 38px;
    color: var(--ink);
    line-height: 1;
  }
  .website .domain { color: var(--maroon); }
</style>
</head>
<body>
<main class="sign">
  <svg class="shapes" width="1200" height="800" viewBox="0 0 1200 800" aria-hidden="true">
    <defs>
      <linearGradient id="panelShade" x1="0" y1="0" x2="1" y2="0">
        <stop offset="0" stop-color="#8a8a8a"/>
        <stop offset="1" stop-color="#6a6a6a"/>
      </linearGradient>
    </defs>
    <line x1="160" y1="97" x2="1040" y2="97" stroke="#6b1014" stroke-width="2"/>
    <polygon points="540,128 1200,128 1200,560 620,560" fill="url(#panelShade)" opacity=".55"/>
    <rect x="598" y="319" width="602" height="7" fill="#ffffff"/>
    <rect x="598" y="471" width="602" height="7" fill="#ffffff"/>
    <polygon points="560,558 1200,558 1200,720 520,720" fill="#e9e9eb"/>
  </svg>

  <h1 class="project-title">BRAMBLEFORD INDUSTRIAL CENTER</h1>

  <svg class="site-photo" width="685" height="116" viewBox="0 0 685 116" role="img" aria-label="Photo of an industrial plant skyline under a blue sky">
    <defs>
      <linearGradient id="photoTone" x1="0" y1="0" x2="0" y2="1">
        <stop offset="0" stop-color="#5f8fc6"/>
        <stop offset=".55" stop-color="#a9c4df"/>
        <stop offset=".8" stop-color="#8d8d86"/>
        <stop offset="1" stop-color="#b59d70"/>
      </linearGradient>
    </defs>
    <polygon points="0,0 685,0 685,116 40,116" fill="url(#photoTone)"/>
  </svg>

  <p class="headline headline--maroon land-for-sale">LAND FOR SALE</p>
  <p class="headline zoning">ZONING:<br>INDUSTRIAL (<span class="code">G I &amp; L I</span>)</p>
  <p class="headline headline--maroon build-to-suit">BUILD TO SUIT</p>

  <div class="inquiry inquiry-label">INQUIRY</div>
  <div class="inquiry inquiry-phone">(555)613-8874</div>

  <div class="brand-mark">
    <span class="brand-square"></span>
    <span class="brand-name">Pillar Ventures Group, Inc.</span>
  </div>
  <p class="company-name">Pillar Ventures Group, Inc.</p>

  <div class="website">WWW.<span class="domain">PILLARVENTURESGROUP</span>.COM</div>
</main>
</body>
</html>
```